'Red Dust Local Roundtable'

We are after a flyer to sell a two day conference to sponsors, delegates and other Councils to participate.
The conference aims to be a forum for Northern Territory Councils to get together and discuss ideas, issues and overcome challenges and isolation in collaboration.
The conference will be a inaugural event with the plan to host a annual two day conference each year with a specific theme relevant to all Northern Territory Councils. - Give the Councils a voice.

```html
<!DOCTYPE html>
<html lang="en">
<head>
<meta charset="utf-8">
<title>Red Dust Local Roundtable – Flyer</title>
<link rel="stylesheet" href="https://fonts.googleapis.com/css2?family=PT+Sans:ital,wght@0,400;0,700;1,400;1,700&family=Delius&display=swap">
<style>
  :root {
    --leaf: #8cc63f;
    --leaf-dash: #9fd05a;
    --sun: #fdbb18;
    --sky: #52b5e8;
    --paper: #ffffff;
    --stage: #f1f1f1;
    --ink: #333333;
    --white: #ffffff;
  }
  * { margin: 0; padding: 0; box-sizing: border-box; }
  html, body { width: 1200px; height: 900px; overflow: hidden; }
  body {
    background: var(--stage);
    font-family: "PT Sans", Arial, sans-serif;
    position: relative;
  }
  .flyer {
    position: absolute;
    left: 300px; top: 25px;
    width: 600px; height: 850px;
    background: var(--paper);
    overflow: hidden;
  }
  .flyer-art { position: absolute; inset: 0; width: 600px; height: 850px; }

  .event-title {
    position: absolute; left: 0; right: 0; top: 36px;
    text-align: center;
    color: var(--white);
    font-weight: 700;
    font-size: 31px;
    letter-spacing: 0.2px;
  }
  .event-date {
    position: absolute; right: 120px; top: 83px;
    color: var(--white);
    font-size: 17px;
  }

  .invite {
    position: absolute;
    left: 98px; width: 400px; top: 270px;
    text-align: center;
    color: var(--white);
  }
  .invite-heading {
    font-family: "Delius", "Comic Sans MS", cursive;
    font-size: 21px;
    font-weight: 400;
    line-height: 1;
    margin-bottom: 7px;
  }
  .invite p {
    font-size: 12.5px;
    line-height: 24.5px;
  }
  .invite .gap { margin-top: 24.5px; }
  .invite em { font-weight: 700; }
  .invite-closing {
    font-family: "Delius", "Comic Sans MS", cursive;
    font-style: normal;
    font-size: 13px;
    opacity: 0.9;
  }

  .council-seal {
    position: absolute;
    left: 40px; top: 650px;
    width: 150px; height: 150px;
    display: flex; align-items: center; justify-content: center;
  }
  .council-name {
    position: relative;
    text-align: center;
    font-weight: 700;
    font-size: 17px;
    line-height: 1.2;
    color: var(--ink);
  }

  .contact {
    position: absolute; left: 222px; top: 668px;
    font-size: 10.5px;
    line-height: 19px;
    color: var(--ink);
  }
  .contact-label { color: var(--leaf); font-style: italic; font-weight: 700; }
  .contact-gap { margin-left: 6px; }

  .website {
    position: absolute; right: 44px; top: 786px;
    color: var(--white);
    font-size: 19px;
  }
</style>
</head>
<body>
  <main class="flyer">
    <svg class="flyer-art" viewBox="0 0 600 850" aria-hidden="true">
      <!-- header band -->
      <path d="M0 0H600V146C450 130 300 150 0 152Z" fill="var(--sky)"/>
      <path d="M0 0H600V140C450 120 300 145 0 146Z" fill="var(--white)"/>
      <path d="M0 0H600V136C450 112 300 140 0 140Z" fill="var(--sun)"/>
      <path d="M0 0H600V122C450 104 300 132 0 128Z" fill="var(--leaf)"/>
      <path d="M0 160C200 150 400 140 600 142" fill="none" stroke="var(--leaf-dash)" stroke-width="1" stroke-dasharray="4 3"/>

      <!-- circles -->
      <circle cx="327" cy="407" r="217" fill="var(--sun)"/>
      <circle cx="257" cy="387" r="213" fill="var(--leaf)"/>
      <circle cx="298" cy="404" r="219" fill="var(--white)"/>
      <circle cx="298" cy="404" r="215" fill="var(--sky)"/>
      <circle cx="298" cy="404" r="207" fill="none" stroke="var(--white)" stroke-width="1" stroke-dasharray="5 4"/>

      <!-- footer band -->
      <path d="M0 712C200 715 400 712 600 690" fill="none" stroke="var(--leaf-dash)" stroke-width="1" stroke-dasharray="4 3"/>
      <path d="M0 722C200 735 400 720 600 700V850H0Z" fill="var(--sky)"/>
      <path d="M0 728C200 740 400 728 600 708V850H0Z" fill="var(--white)"/>
      <path d="M0 731C200 743 400 732 600 712V850H0Z" fill="var(--sun)"/>
      <path d="M0 740C200 752 400 742 600 724V850H0Z" fill="var(--leaf)"/>
    </svg>

    <h1 class="event-title">“Red Dust Local Roundtable”</h1>
    <p class="event-date">13-14 April 2011</p>

    <section class="invite">
      <h2 class="invite-heading">You’re invited to attend</h2>
      <p>The “Red Dust Local Roundtable” conference.</p>
      <p class="gap">The conference aims to provide a forum for Northern Territory<br>Councils to get together and discuss ideas which will enable<br>us to overcome the challenges of isolation.</p>
      <p class="gap">The conference will be for <em><i>all</i></em> Northern Territory Councils -<br>giving <em><i>all</i></em> Councils a voice.</p>
      <p class="gap invite-closing">Let’s work together to secure our future.</p>
    </section>

    <div class="council-seal">
      <svg style="position:absolute;inset:0" viewBox="0 0 150 150" aria-hidden="true">
        <circle cx="75" cy="75" r="72" fill="var(--white)"/>
      </svg>
      <p class="council-name">Stringybark<br>Shire Council</p>
    </div>

    <div class="contact">
      <p>For more information contact Mara Tindall:</p>
      <p><span class="contact-label">Phone:</span> 08 8900 4172 <span class="contact-label contact-gap">Email:</span> mara.tindall@stringybark.nt.gov.au</p>
    </div>

    <p class="website">www.stringybarkshire.net.au</p>
  </main>
</body>
</html>
```